Local Flower Farm Needs Business Card Design

I need business cards designed for a flower farm based in Eudora, Kansas.
Business Info:
We are a local cut flower farm located in Eudora, Kansas, founded by Darla Hoffstrom. What started as a passion for agriculture and search for more joy in daily life has blossomed into a small business dedicated to providing the community with beautiful, fresh, and sustainable flowers. We specialize in local, seasonal blooms, ensuring that every petal reflects the care and dedication we pour into our craft. Our mission is to deliver the highest quality flowers directly to our customers through local farmers markets and to florists who share our commitment to sustainability. Join us in celebrating the beauty of nature, one bloom at a time!
Contact Details:
Darla Hoffstrom
Owner
Phone 913-555-0147
Facebook: Lorabelle Quinn Blossoms
Instagram: @LorabelleQuinnBlossoms
Website: LorabelleQuinnBlossoms.example
Target Market(s)
Wholesale to Florists and Direct to Consumer via Farmers Market
Industry/Entity Type
Florist, Farm
Contact Information for Business Card
Name, Contact Info, Logo
Look and feel

```html
<!DOCTYPE html>
<html lang="en">
<head>
<meta charset="utf-8">
<title>Lorabelle Quinn Blossoms – Business Card</title>
<link rel="stylesheet" href="https://fonts.googleapis.com/css2?family=Montserrat:wght@400;500;700&display=swap">
<style>
  :root {
    --page: #ece8e1;
    --card-front: #ffffff;
    --card-back: #0b2a2f;
    --ink: #0d3336;
    --ink-soft: #1f2b2d;
    --emboss: #164248;
    --emboss-line: #1d4d53;
  }
  * { margin: 0; padding: 0; box-sizing: border-box; }
  html, body { width: 900px; height: 1200px; overflow: hidden; }
  body {
    background: var(--page);
    font-family: "Montserrat", Arial, sans-serif;
    color: var(--ink);
    position: relative;
  }
  .card {
    position: absolute;
    left: 80px;
    width: 742px;
    height: 440px;
    border-radius: 24px;
  }
  .card-front { top: 131px; background: var(--card-front); box-shadow: 0 2px 6px rgba(0,0,0,.12); }
  .card-back { top: 640px; background: var(--card-back); }

  .brand-seal {
    position: absolute;
    left: 34px; top: 38px;
    width: 226px; height: 226px;
    border: 1.5px solid var(--ink-soft);
    border-radius: 50%;
    display: flex; align-items: center; justify-content: center;
    text-align: center;
  }
  .brand-name {
    font-family: "Montserrat", Arial, sans-serif;
    font-weight: 700;
    color: var(--ink);
    text-transform: uppercase;
    letter-spacing: 2px;
  }
  .brand-seal .brand-name { font-size: 19px; line-height: 1.35; }

  .owner {
    position: absolute;
    right: 50px; top: 44px;
    text-align: right;
  }
  .owner-name { font-size: 26px; font-weight: 700; color: var(--ink); letter-spacing: .2px; }
  .owner-title { font-size: 16px; font-weight: 400; color: var(--ink-soft); margin-top: 3px; }

  .brand-feature {
    position: absolute;
    right: 52px; top: 196px;
    width: 210px;
    text-align: left;
  }
  .brand-feature .brand-name { font-size: 30px; line-height: 1.15; letter-spacing: 1px; }

  .contact-list {
    position: absolute;
    left: 36px; top: 307px;
    list-style: none;
  }
  .contact-list li {
    display: flex; align-items: center;
    font-size: 16px; color: var(--ink-soft);
    height: 26px;
  }
  .contact-list svg { width: 16px; height: 16px; margin-right: 8px; flex: none; }

  .back-seal {
    position: absolute;
    left: 201px; top: 50px;
    width: 340px; height: 340px;
    border: 2px solid var(--emboss-line);
    border-radius: 50%;
    display: flex; align-items: center; justify-content: center;
    text-align: center;
  }
  .back-seal .brand-name { color: var(--emboss); font-size: 34px; line-height: 1.3; letter-spacing: 3px; }
</style>
</head>
<body>
  <section class="card card-front">
    <div class="brand-seal">
      <span class="brand-name">Lorabelle<br>Quinn<br>Blossoms</span>
    </div>

    <div class="owner">
      <div class="owner-name">Darla Hoffstrom</div>
      <div class="owner-title">Owner</div>
    </div>

    <div class="brand-feature">
      <span class="brand-name">Lorabelle<br>Quinn<br>Blossoms</span>
    </div>

    <ul class="contact-list">
      <li>
        <svg viewBox="0 0 16 16" aria-hidden="true"><path d="M4 1.5l2.2 3-1.3 1.5c.8 1.8 2.3 3.3 4.1 4.1l1.5-1.3 3 2.2-1.2 2.5C7.3 13.3 2.7 8.7 1.5 3.7z" fill="none" stroke="var(--ink-soft)" stroke-width="1.5" stroke-linejoin="round"/></svg>
        913-555-0147
      </li>
      <li>
        <svg viewBox="0 0 16 16" aria-hidden="true"><circle cx="8" cy="8" r="7" fill="var(--ink-soft)"/></svg>
        Lorabelle Quinn Blossoms
      </li>
      <li>
        <svg viewBox="0 0 16 16" aria-hidden="true"><rect x="1.5" y="1.5" width="13" height="13" rx="3" fill="var(--ink-soft)"/></svg>
        @LorabelleQuinnBlossoms
      </li>
      <li>
        <svg viewBox="0 0 16 16" aria-hidden="true"><circle cx="8" cy="8" r="6.8" fill="none" stroke="var(--ink-soft)" stroke-width="1.4"/><ellipse cx="8" cy="8" rx="3" ry="6.8" fill="none" stroke="var(--ink-soft)" stroke-width="1.2"/><path d="M1.2 8h13.6" stroke="var(--ink-soft)" stroke-width="1.2"/></svg>
        www.LorabelleQuinnBlossoms.example
      </li>
    </ul>
  </section>

  <section class="card card-back">
    <div class="back-seal">
      <span class="brand-name">Lorabelle<br>Quinn<br>Blossoms</span>
    </div>
  </section>
</body>
</html>
```